K Velmor Architectural Construction & Abatement, Inc.
K Velmor Architectural Construction, Inc.
Pilo 47:
86# Has very little orange. Use these colors please. Read all the reviews I gave other designers. Incorporate these ideas into to your design. Push forth these ideas.
Thank you,
rovatique:
Use more green color. Green on back of the card. And on stationary. Continue to push forth with these ideas.
Trulsen:
# 83 Remove the fax information on stationary
# 83 remove the black color on cards & Stationary. Use the original colors. Place motto on back as well.
Use little more green color on front. Green Energy feel. Use the orange as well. Put the logos on envelopes.
erovatique:
Please, include my education on the business cards. BArch, MArch. Thank You.
Pilo47:
Please, find away to include my education details on my business cards: BArch, MArch
I like some of the cards you have put together so far. And I have selected my favorites my star rating system. I asked that the front remain the same. But, the back have another logo which says K Velmor Architect ABATEMENT. I will upload the design for the business cards. Continue, to push the ideas.

```html
<!DOCTYPE html>
<html lang="en">
<head>
<meta charset="utf-8">
<title>K Velmor Architects — Business Cards</title>
<link rel="stylesheet" href="https://fonts.googleapis.com/css2?family=PT+Sans:ital,wght@0,400;0,700;1,700&display=swap">
<style>
  :root {
    --bg: #e9e6e1;
    --card: #ffffff;
    --orange: #f26a1b;
    --green: #6cbf2a;
    --blue: #2a6fb5;
    --text: #4a4a4a;
    --rule: #9a9a9a;
  }
  * { margin: 0; padding: 0; box-sizing: border-box; }
  html, body { width: 1200px; height: 852px; overflow: hidden; }
  body {
    background: var(--bg);
    font-family: "PT Sans", Arial, sans-serif;
    color: var(--text);
    position: relative;
  }
  .card {
    position: absolute;
    width: 560px;
    height: 320px;
    background: var(--card);
    border-radius: 16px;
    overflow: hidden;
    box-shadow: 0 6px 18px rgba(0,0,0,0.18);
  }
  .card--horizontal { left: 70px; top: 70px; }
  .card--stacked { left: 570px; top: 462px; }
  .card__swoosh { position: absolute; inset: 0; width: 100%; height: 100%; }

  .brand { position: absolute; display: flex; align-items: center; gap: 10px; }
  .brand__mark { width: 30px; height: 30px; background: var(--orange); border-radius: 4px; flex: none; }
  .brand__name {
    font-weight: 700;
    font-size: 40px;
    line-height: 1;
    color: var(--green);
    letter-spacing: 0.5px;
  }

  .card--horizontal .brand { left: 140px; top: 92px; }
  .card--horizontal .person {
    position: absolute; left: 150px; top: 172px;
    font-size: 19px; white-space: nowrap;
  }
  .person__name { color: var(--blue); font-weight: 700; }
  .person__sep { color: var(--blue); margin: 0 6px; }
  .person__role { color: var(--green); font-weight: 700; font-style: italic; font-size: 16px; }

  .contact { position: absolute; display: flex; font-size: 15px; line-height: 1.5; }
  .card--horizontal .contact { left: 150px; top: 210px; }
  .contact__address { font-style: normal; padding-right: 16px; border-right: 1px solid var(--rule); }
  .contact__lines { padding-left: 12px; }
  .contact__line { display: flex; align-items: center; gap: 6px; white-space: nowrap; }
  .contact__icon { width: 14px; height: 14px; flex: none; }

  .card--stacked .brand { left: 40px; top: 128px; }
  .card--stacked .brand__name { font-size: 34px; width: 190px; line-height: 1.05; }
  .card--stacked .person {
    position: absolute; left: 300px; top: 66px;
    font-size: 19px; line-height: 1.25;
  }
  .card--stacked .person__role { display: block; font-size: 15px; }
  .card--stacked .contact {
    left: 300px; top: 146px; flex-direction: column;
    padding-left: 12px; border-left: 1px solid var(--rule);
  }
  .card--stacked .contact__address { border: 0; padding: 0 0 6px 0; }
  .card--stacked .contact__lines { padding: 0; }
</style>
</head>
<body>

<section class="card card--horizontal" aria-label="Business card, horizontal layout">
  <svg class="card__swoosh" viewBox="0 0 560 320" preserveAspectRatio="none" aria-hidden="true">
    <path d="M0 110 C 40 190, 70 260, 150 320 L 0 320 Z" fill="var(--green)"/>
    <path d="M0 140 C 30 210, 55 268, 120 320 L 0 320 Z" fill="var(--orange)"/>
  </svg>
  <div class="brand">
    <span class="brand__mark"></span>
    <span class="brand__name">K Velmor Architects</span>
  </div>
  <p class="person">
    <span class="person__name">Marcus Hale</span><span class="person__sep">/</span><span class="person__role">Architect Intern / Project Manager</span>
  </p>
  <div class="contact">
    <address class="contact__address">2210 Orchard Ln West<br>Belford, Texas 77102</address>
    <div class="contact__lines">
      <p class="contact__line">
        <svg class="contact__icon" viewBox="0 0 14 14" aria-hidden="true"><rect x="3" y="1" width="8" height="12" rx="1.5" fill="var(--blue)"/><rect x="4.5" y="3" width="5" height="6" fill="#fff"/></svg>
        (555) 214-7730
      </p>
      <p class="contact__line">
        <svg class="contact__icon" viewBox="0 0 14 14" aria-hidden="true"><circle cx="7" cy="7" r="5.5" fill="none" stroke="var(--blue)" stroke-width="1.6"/><circle cx="7" cy="7" r="2" fill="none" stroke="var(--blue)" stroke-width="1.6"/></svg>
        kvelmorconstr@mailbox.com
      </p>
    </div>
  </div>
</section>

<section class="card card--stacked" aria-label="Business card, stacked layout">
  <svg class="card__swoosh" viewBox="0 0 560 320" preserveAspectRatio="none" aria-hidden="true">
    <path d="M470 0 C 510 80, 535 180, 560 240 L 560 0 Z" fill="var(--green)"/>
    <path d="M500 0 C 530 70, 548 150, 560 200 L 560 0 Z" fill="var(--orange)"/>
    <path d="M0 250 C 20 280, 40 305, 60 320 L 0 320 Z" fill="var(--orange)"/>
  </svg>
  <div class="brand">
    <span class="brand__mark"></span>
    <span class="brand__name">K Velmor Architects</span>
  </div>
  <p class="person">
    <span class="person__name">Marcus Hale</span>
    <span class="person__role">Architect Intern<br>Project Manager</span>
  </p>
  <div class="contact">
    <address class="contact__address">2210 Orchard Ln West<br>Belford, Texas 77102</address>
    <div class="contact__lines">
      <p class="contact__line">
        <svg class="contact__icon" viewBox="0 0 14 14" aria-hidden="true"><rect x="3" y="1" width="8" height="12" rx="1.5" fill="var(--blue)"/><rect x="4.5" y="3" width="5" height="6" fill="#fff"/></svg>
        (555) 214-7730
      </p>
      <p class="contact__line">
        <svg class="contact__icon" viewBox="0 0 14 14" aria-hidden="true"><circle cx="7" cy="7" r="5.5" fill="none" stroke="var(--blue)" stroke-width="1.6"/><circle cx="7" cy="7" r="2" fill="none" stroke="var(--blue)" stroke-width="1.6"/></svg>
        kvelmorconstr@mailbox.com
      </p>
    </div>
  </div>
</section>

</body>
</html>
```